Business Card Re-Design for a Lighting Designer

I would like my business card re-designed. It is currently high gloss and they scratch too easily. I don not think the current design lends itself well to a matte finish. I have included the current design for reference along with our company logo.
Check out our website for current branding.
http://www.brenmoorastudio.example

Updates
Some of the top contenders are muslim and it is a holiday for them. I do not want to discriminate and would expect the same courtesy for holidays we celebrate.
Target Market(s)
Interior Designers, Architects
Contact Information for Business Card
Logo - Name, Title, Address, Telephone Number and Extension, Email
Font styles to use
Requirements
Must have
- All the information listed on the current business card. If you use Red, it needs to be the red from our logo.
Nice to have
- Vertical and Horizontal Designs will be entertained.
Should not have
- Requirements for a glossy finish...should not look too corporate since we are a design firm.

```html
<!DOCTYPE html>
<html lang="en">
<head>
<meta charset="utf-8">
<title>Bren Moora Studio — Business Cards</title>
<link rel="stylesheet" href="https://fonts.googleapis.com/css2?family=Montserrat:wght@400;500;700&display=swap">
<style>
  :root {
    --backdrop: #d4d4d4;
    --brand-red: #9b1b1f;
    --brand-red-deep: #7e1014;
    --brand-blush: #f0c2a8;
    --ink: #2b2b2b;
    --muted: #8a8a8a;
    --paper: #ffffff;
  }
  * { margin: 0; padding: 0; box-sizing: border-box; }
  html, body { width: 1200px; height: 900px; overflow: hidden; }
  body {
    background: var(--backdrop);
    font-family: "Montserrat", sans-serif;
    position: relative;
  }

  /* Reverse side: landscape */
  .card-back {
    position: absolute;
    left: 60px; top: 290px;
    width: 560px; height: 320px;
    background: var(--brand-red);
    box-shadow: 0 6px 18px rgba(0,0,0,0.18);
    overflow: hidden;
  }
  .card-back__glow {
    position: absolute;
    left: 120px; top: 16px;
    width: 424px; height: 210px;
    background: linear-gradient(100deg, var(--brand-blush) 0%, #d9483a 22%, #a41d22 48%, var(--brand-red-deep) 100%);
  }
  .card-back__tagline {
    position: absolute;
    left: 28px; bottom: 24px;
    color: var(--paper);
    font-size: 13px;
    font-weight: 500;
    letter-spacing: 0.12em;
  }

  /* Front side: portrait */
  .card-front {
    position: absolute;
    left: 720px; top: 170px;
    width: 340px; height: 560px;
    background: var(--paper);
    box-shadow: 0 6px 18px rgba(0,0,0,0.18);
    padding: 44px 30px 0 30px;
  }
  .brand {
    display: flex;
    align-items: center;
    justify-content: flex-end;
    gap: 12px;
  }
  .brand__square {
    width: 22px; height: 22px;
    background: var(--brand-red);
    flex: none;
  }
  .brand__name {
    font-size: 24px;
    font-weight: 500;
    color: var(--ink);
    letter-spacing: 0.04em;
    line-height: 1.1;
  }
  .brand__tagline {
    margin-top: 10px;
    padding-top: 8px;
    border-top: 1px solid #e2a6a8;
    text-align: right;
    font-size: 10px;
    letter-spacing: 0.14em;
    color: var(--muted);
  }

  .person { margin-top: 170px; }
  .person__name {
    color: var(--brand-red);
    font-weight: 700;
    font-size: 20px;
    letter-spacing: 0.02em;
  }
  .person__title {
    font-size: 13px;
    color: var(--ink);
    letter-spacing: 0.04em;
    padding-bottom: 10px;
    border-bottom: 1px solid #cfcfcf;
  }
  .address {
    margin-top: 14px;
    font-size: 12.5px;
    line-height: 1.5;
    color: var(--ink);
    font-style: normal;
  }
  .contact { list-style: none; margin-top: 14px; }
  .contact__row {
    display: flex; align-items: center; gap: 8px;
    font-size: 12.5px; color: var(--ink); line-height: 1.7;
  }
  .contact__row--web { font-weight: 700; }
  .contact__icon { width: 12px; height: 12px; flex: none; }
</style>
</head>
<body>

  <section class="card-back" aria-label="Card reverse">
    <div class="card-back__glow" role="img" aria-label="Soft red light gradient field"></div>
    <p class="card-back__tagline">LIGHTING FOR ARCHITECTURE</p>
  </section>

  <section class="card-front" aria-label="Card front">
    <div class="brand">
      <span class="brand__name">BREN MOORA STUDIO</span>
      <span class="brand__square" aria-hidden="true"></span>
    </div>
    <p class="brand__tagline">LIGHTING FOR ARCHITECTURE</p>

    <div class="person">
      <h1 class="person__name">MARISOL DEVERAUX</h1>
      <p class="person__title">PRINCIPAL</p>
    </div>

    <address class="address">
      412 Calder Row, Suite 210<br>
      Larkfield, Georgia 30999
    </address>

    <ul class="contact">
      <li class="contact__row">
        <svg class="contact__icon" viewBox="0 0 12 12" aria-hidden="true"><path d="M2.5 1h2l1 2.5-1.3 1a6 6 0 0 0 3.3 3.3l1-1.3L11 7.5v2A1.5 1.5 0 0 1 9.5 11 8.5 8.5 0 0 1 1 2.5 1.5 1.5 0 0 1 2.5 1z" fill="var(--brand-red)"/></svg>
        555.014.2280 x1
      </li>
      <li class="contact__row">
        <svg class="contact__icon" viewBox="0 0 12 12" aria-hidden="true"><rect x="0.8" y="2.3" width="10.4" height="7.4" fill="none" stroke="var(--brand-red)" stroke-width="1.2"/><path d="M1 2.6l5 4 5-4" fill="none" stroke="var(--brand-red)" stroke-width="1.2"/></svg>
        marisol@brenmoorastudio.example
      </li>
      <li class="contact__row contact__row--web">
        <svg class="contact__icon" viewBox="0 0 12 12" aria-hidden="true"><circle cx="6" cy="6" r="5" fill="none" stroke="var(--brand-red)" stroke-width="1.2"/><path d="M1 6h10M6 1c-2.4 2.8-2.4 7.2 0 10M6 1c2.4 2.8 2.4 7.2 0 10" fill="none" stroke="var(--brand-red)" stroke-width="1"/></svg>
        www.brenmoorastudio.example
      </li>
    </ul>
  </section>

</body>
</html>
```